Business Card Design Project

Business card for new event planning company. I will load in 2 different colors of logs for you to use.

Target Market(s)

meeting planners and business leaders

Industry/Entity Type

Event Planning

Requirements
Must have
• memorable/ creative please - maybe logo on back of the card

Information for business card: (Information may change)

LaVonna Birchwell
lav@MarigoldOccasionsandGatherings.com
www.MarigoldOccasionsandGatherings.com
555.730.2964
Nice to have
• Do you think it would be too much to add twiiter, FB, linked in logo to card to connect?

all are LaVonna Birchwell

```html
<!DOCTYPE html>
<html lang="en">
<head>
<meta charset="utf-8">
<title>Marigold Occasions&amp;Gatherings — Business Card</title>
<link href="https://fonts.googleapis.com/css2?family=EB+Garamond:wght@400;500&display=swap" rel="stylesheet">
<style>
  :root {
    --canvas: #e9e6e2;
    --card-dark: #2b2528;
    --card-dark-edge: #1f1a1c;
    --card-light: #f7f7f6;
    --ink: #2e2b2b;
    --ink-soft: #4a4646;
    --rule: #3a3636;
    --periwinkle: #8a9ae0;
    --orange: #ee7c31;
    --logo-blue: #6f7fcf;
  }
  * { box-sizing: border-box; margin: 0; padding: 0; }
  html, body {
    width: 1200px; height: 900px; overflow: hidden;
    background: var(--canvas);
    font-family: "EB Garamond", Georgia, serif;
  }
  .stage {
    position: relative; width: 1200px; height: 900px;
    display: flex; justify-content: center; align-items: center; gap: 90px;
  }
  .card {
    position: relative; width: 400px; height: 700px;
    box-shadow: 0 10px 30px rgba(0,0,0,0.18);
  }
  /* Front */
  .card--front {
    background: radial-gradient(ellipse at 60% 40%, #3a3236 0%, var(--card-dark) 55%, var(--card-dark-edge) 100%);
  }
  .dot-motif {
    position: absolute; left: 70px; top: 70px; width: 270px; height: 240px;
    border-radius: 40px;
    background: linear-gradient(160deg, var(--periwinkle) 0%, var(--periwinkle) 42%, var(--orange) 58%, var(--orange) 100%);
    opacity: 0.9;
  }
  .front-brand {
    position: absolute; left: 40px; bottom: 110px;
    display: flex; align-items: center; gap: 12px;
  }
  .brand-mark {
    width: 18px; height: 18px; border-radius: 50%;
    background: var(--orange); flex: none;
  }
  .brand-name {
    font-weight: 500; font-size: 24px; line-height: 1.15;
    color: var(--logo-blue);
  }
  /* Back */
  .card--back { background: var(--card-light); }
  .back-brand {
    position: absolute; right: 50px; top: 60px;
    display: flex; align-items: center; gap: 8px;
  }
  .back-brand .brand-name { font-size: 17px; }
  .back-brand .brand-mark { width: 12px; height: 12px; }
  .contact {
    position: absolute; left: 50px; right: 50px; top: 190px;
    color: var(--ink);
  }
  .contact__name {
    font-size: 27px; font-weight: 500; letter-spacing: 0.3px;
    text-align: right; padding-bottom: 10px;
  }
  .contact__rule { border: 0; border-top: 1.5px solid var(--rule); margin: 0 0 18px; }
  .contact__list { list-style: none; font-size: 15.5px; line-height: 1.85; color: var(--ink-soft); margin-bottom: 18px; }
</style>
</head>
<body>
<main class="stage">
  <section class="card card--front" aria-label="Card front">
    <div class="dot-motif" role="img" aria-label="Decorative pattern of blue and orange dots"></div>
    <div class="front-brand">
      <span class="brand-mark"></span>
      <span class="brand-name">Marigold<br>Occasions&amp;Gatherings</span>
    </div>
  </section>

  <section class="card card--back" aria-label="Card back">
    <div class="back-brand">
      <span class="brand-mark"></span>
      <span class="brand-name">Marigold Occasions&amp;Gatherings</span>
    </div>
    <div class="contact">
      <h1 class="contact__name">LaVonna Birchwell</h1>
      <hr class="contact__rule">
      <ul class="contact__list">
        <li>E: lav@MarigoldOccasionsandGatherings.com</li>
        <li>W: www.MarigoldOccasionsandGatherings.com</li>
        <li>M: 555.730.2964</li>
      </ul>
      <hr class="contact__rule">
      <ul class="contact__list">
        <li>F: friendspace.net/LaVonna Birchwell</li>
        <li>T: chirpline.net/LaVonna Birchwell</li>
        <li>In: workcircle.net/LaVonna Birchwell</li>
      </ul>
      <hr class="contact__rule">
    </div>
  </section>
</main>
</body>
</html>
```